Celebrate February in The Bluevales at Meadow Ripple Waterpark Resort

Create something similar to the attached design - can very and be creative but the overall concept is one I would like to recreate
Celebrate February in The Bluevales
Meadow Ripple logo (at top)
Romantic Rooms, Family Suites, Free Buffet Breakfast included, Indoor Pool and Parkway Convenience
Low Rates!

866.452.0298 MeadowRipple.example/

I have attached logos and pictures to use

Target Market(s)

Email customers to entice them to come to the bluevales in February ..

Industry/Entity Type

Hospitality

Requirements
Must have
• phone number 866.452.0298
• website MeadowRipple.example/
Nice to have
• a romantic feel but not to much so .. families and couples can both enjoy the area in february

```html
<!DOCTYPE html>
<html lang="en">
<head>
<meta charset="utf-8">
<title>Celebrate February in The Bluevales — Meadow Ripple Waterpark Resort</title>
<link rel="stylesheet" href="https://fonts.googleapis.com/css2?family=Playfair+Display:wght@400;700&family=Montserrat:wght@400;500;600&display=swap">
<style>
:root{
  --red:#e8141b;
  --ink:#1d1d1f;
  --muted:#555a60;
  --lavender:#eceef6;
  --page:#ffffff;
  --navy:#1c2f4a;
  --footer:#efeff1;
}
*{box-sizing:border-box;margin:0;padding:0}
html,body{width:1200px;height:1200px;overflow:hidden;background:var(--page)}
body{font-family:"Playfair Display",Georgia,serif;color:var(--ink);position:relative}
.email{position:absolute;left:453px;top:0;width:296px;height:1200px;background:var(--page);overflow:hidden}
.abs{position:absolute}

/* hero */
.hero{left:0;top:0;width:296px;height:266px;background:linear-gradient(180deg,#f3f2f6 0%,#e9e7ee 45%,#f4f4f6 80%,#fbfbfc 100%)}
.hero-photo{left:18px;top:45px;width:260px;height:190px;border-radius:6px;background:radial-gradient(ellipse at 50% 55%,#d7d3d4 0%,#e6e3e7 45%,rgba(240,239,243,0) 75%)}
.hero-headboard{left:20px;top:140px;width:256px;height:45px;background:linear-gradient(90deg,#1f3d57,#2a4a66);border-radius:6px;opacity:.85}
.hero-bed{left:0;top:180px;width:296px;height:86px;background:linear-gradient(180deg,#f1f1f3,#fbfbfc)}
.brand-mark{left:11px;top:10px;display:flex;align-items:center;gap:3px;font-size:6px;font-weight:700;color:var(--navy)}
.brand-mark i{display:block;width:14px;height:14px;border-radius:50%;background:#7a1b1b}
.call{left:148px;top:14px;font-family:"Montserrat",Arial,sans-serif;font-size:8px;color:var(--ink);font-weight:500}
.call b{color:var(--red);font-weight:600}
.book{left:231px;top:12px;width:51px;height:15px;background:var(--red);color:#fff;font-family:"Montserrat",Arial,sans-serif;font-size:7px;display:flex;align-items:center;justify-content:center}
.title-box{left:38px;top:72px;width:220px;height:58px;border:1px solid rgba(255,255,255,.9);background:rgba(255,255,255,.45);display:flex;align-items:center;justify-content:center;text-align:center;font-size:17px;line-height:21px;font-weight:400;color:#111;padding:0 8px}
.red-rule{width:1px;background:var(--red)}
.read-more{left:119px;top:154px;width:57px;height:18px;border:1px solid #fff;background:rgba(30,40,55,.55);color:#fff;font-size:8px;font-weight:700;display:flex;align-items:center;justify-content:center}

/* what we do */
.what{left:0;top:266px;width:296px;height:151px;background:var(--lavender)}
.thumb{width:49px;height:49px;border:2px solid #fff}
.what-copy{left:140px;top:30px;width:135px}
.what-copy h2{font-size:10px;font-weight:700}
.what-copy .tick{display:block;width:1px;height:11px;background:var(--ink);margin:4px 0 8px}
.what-copy p{font-size:7px;line-height:12.3px;color:var(--muted)}
.what-copy a{font-size:7px;font-weight:700;color:var(--red);text-decoration:none}

/* gallery */
.gallery-title{left:148px;top:440px;font-size:10px;font-weight:700}
.gallery-row{left:0;width:296px;height:88px}
.tile-img{position:absolute;top:0;width:148px;height:88px}
.tile-copy{position:absolute;top:0;width:148px;height:88px;padding:0 15px;display:flex;flex-direction:column;justify-content:center}
.tile-copy h3{font-size:10px;font-weight:400;line-height:13px;margin-bottom:4px}
.tile-copy p{font-size:7px;line-height:11.5px;color:var(--muted)}
.tile-copy.right-aligned{text-align:right}
.arrow-box{position:absolute;left:47px;top:34px;width:54px;height:20px;border:1px solid #fff}

/* signup */
.signup{left:0;top:935px;width:296px;height:115px;background:linear-gradient(160deg,#3b4a32 0%,#25301f 50%,#4a3a2c 100%)}
.signup h2{position:absolute;left:0;top:24px;width:296px;text-align:center;font-size:12px;font-weight:400;color:#fff}
.signup .red-rule{position:absolute;left:148px;top:45px;height:12px;background:#fff;opacity:.7}
.signup-field{left:40px;top:70px;width:215px;height:19px;display:flex;border-radius:10px;overflow:hidden}
.signup-field span{flex:1;background:#fff;font-size:6px;color:#888;display:flex;align-items:center;padding-left:8px}
.signup-field b{width:61px;background:var(--red);color:#fff;font-size:6.5px;font-weight:400;display:flex;align-items:center;justify-content:center}

/* footer */
.footer{left:0;top:1050px;width:296px;height:126px;background:var(--footer)}
.footer-brand{left:0;top:24px;width:296px;text-align:center;font-size:12px;font-weight:700;color:var(--navy)}
.footer-brand small{display:block;font-family:"Montserrat",Arial,sans-serif;font-size:6px;font-weight:400;letter-spacing:.5px;margin-top:2px}
.footer-phone{left:0;top:71px;width:296px;display:flex;justify-content:center;align-items:center;gap:5px;font-family:"Montserrat",Arial,sans-serif;font-size:10px}
.footer-social{left:0;top:97px;width:296px;display:flex;justify-content:center;gap:5px}
.footer-social i{display:block;width:6px;height:6px;border-radius:50%;background:var(--ink)}
.copyright{left:0;top:1176px;width:296px;height:24px;border-top:1px solid #ddd;background:var(--footer);text-align:center;font-family:"Montserrat",Arial,sans-serif;font-size:6px;line-height:20px}
</style>
</head>
<body>
<main class="email">

  <header class="abs hero">
    <div class="abs hero-photo" role="img" aria-label="Photo of a smiling couple stretching in bed after waking up"></div>
    <div class="abs hero-headboard" role="img" aria-label="Navy upholstered headboard"></div>
    <div class="abs hero-bed" role="img" aria-label="White bed linen"></div>
    <div class="abs brand-mark"><i></i>Meadow Ripple</div>
    <div class="abs call"><b>Call:</b> 866.452.0298</div>
    <div class="abs book">BOOK NOW</div>
    <h1 class="abs title-box">Celebrate February in The Bluevales</h1>
    <div class="abs red-rule" style="left:147px;top:130px;height:19px"></div>
    <div class="abs read-more">Read More</div>
  </header>

  <section class="abs what">
    <div class="abs thumb" style="left:21px;top:24px;background:linear-gradient(135deg,#d9d2c8,#5a4438)" role="img" aria-label="Loft suite with spiral staircase"></div>
    <div class="abs thumb" style="left:74px;top:24px;background:linear-gradient(135deg,#1b2330,#3a4e6c)" role="img" aria-label="Rafting group on the river"></div>
    <div class="abs thumb" style="left:21px;top:78px;background:linear-gradient(135deg,#4e7a6a,#9fd3c6)" role="img" aria-label="Guest room with teal bedding"></div>
    <div class="abs thumb" style="left:74px;top:78px;background:linear-gradient(135deg,#3f7a3a,#e25a3b)" role="img" aria-label="Colourful waterpark play structure"></div>
    <div class="abs what-copy">
      <h2>What we Do</h2>
      <span class="tick"></span>
      <p>With over 75,000 gallons of water, the Meadow Ripple Waterpark is your vacation destination. Whether it's the 4-story twi and turns of the River Run</p>
      <a href="#">Read Maore...</a>
    </div>
  </section>

  <h2 class="abs gallery-title">Gallery</h2>
  <div class="abs red-rule" style="left:148px;top:458px;height:10px"></div>

  <section class="abs gallery-row" style="top:478px">
    <div class="tile-img" style="left:0;background:linear-gradient(160deg,#8a8f98,#2c3a52 60%,#b65a2c)" role="img" aria-label="Romantic room with king bed and patterned carpet"></div>
    <div class="tile-copy" style="left:148px">
      <h3>Romantic Rooms</h3>
      <p>Enjoy spacious hospitality in this room with one King bed.</p>
    </div>
  </section>

  <section class="abs gallery-row" style="top:566px">
    <div class="tile-copy right-aligned" style="left:0">
      <h3>Family Suites</h3>
      <p>Pine Hollow Outfitters, Inc. is a rafting company located</p>
    </div>
    <div class="tile-img" style="left:148px;background:linear-gradient(160deg,#1a222e,#2e3d55 60%,#1c2a3e)" role="img" aria-label="Family rafting on the river">
      <svg class="arrow-box" viewBox="0 0 54 20" aria-hidden="true"><path d="M20 10h14M29 5l5 5-5 5" fill="none" stroke="#fff" stroke-width="1.2"/></svg>
    </div>
  </section>

  <section class="abs gallery-row" style="top:654px">
    <div class="tile-img" style="left:0;background:linear-gradient(170deg,#c9cfa8,#eef0e6 45%,#6c7178)" role="img" aria-label="Coffee cup on a table in morning light"></div>
    <div class="tile-copy" style="left:148px">
      <h3>Free Buffet Breakfast included</h3>
      <p>Enjoy spacious hospitality in this room with one King bed.</p>
    </div>
  </section>

  <section class="abs gallery-row" style="top:742px">
    <div class="tile-copy right-aligned" style="left:0">
      <h3>Indoor Pool</h3>
      <p>Warm water and slides for the whole family all winter long</p>
    </div>
    <div class="tile-img" style="left:148px;background:linear-gradient(170deg,#9fd4e8,#4fa6cf 55%,#2f6f95)" role="img" aria-label="Indoor heated pool with slides"></div>
  </section>

  <section class="abs gallery-row" style="top:830px">
    <div class="tile-img" style="left:0;background:linear-gradient(170deg,#3d6b34,#7fb24a 45%,#7fc4e0)" role="img" aria-label="Waterpark play structure with slides"></div>
    <div class="tile-copy" style="left:148px">
      <h3>Parkway Convenience<br>Low Rates!</h3>
      <p>Pine Hollow Outfitters, Inc. is a rafting company located</p>
    </div>
  </section>

  <section class="abs signup" role="img" aria-label="Mountain forest with wooden coaster in the background">
    <h2>Email customers to the bluevales</h2>
    <div class="red-rule"></div>
    <div class="abs signup-field"><span>Enter your email</span><b>SEND EMAIL</b></div>
  </section>

  <footer class="abs footer">
    <div class="abs footer-brand">Meadow Ripple<small>WATERPARK RESORT</small></div>
    <div class="abs footer-phone">
      <svg width="14" height="12" viewBox="0 0 14 12" aria-hidden="true"><path d="M3 1.5l2 2-1 1.5c.7 1.5 1.9 2.7 3.4 3.4L9 7.4l2 2-1.5 1.5C5.5 10.5 2 7 1.5 3z" fill="none" stroke="var(--red)" stroke-width="1"/></svg>
      <span style="color:var(--red)">–</span> 866.452.0298
    </div>
    <div class="abs footer-social" aria-label="Social links"><i></i><i></i><i></i><i></i></div>
  </footer>
  <div class="abs copyright">@MeadowRipple.example 2019</div>

</main>
</body>
</html>
```